Naturopath Practitioner Card Design

I am a naturopath needing a design for a business card mainly to show that I am a naturopath and have some contact details to give to prospective clients. I am open minded about the design and what is on the second side of the card whether it just be some artwork or space for details, appointment times etc. Naturopathy is the practice of natural medicine that uses a holistic approach and incorporates herbal and nutritional medicine.

Industry/Entity Type

Business

Contact Information for Business Card

Tom Welby NaturopathBHSc (Naturopathy) Member PHRA 0492 815 306 tom.welby@mailbright.com www.tomwelbynaturopathy.com.au

Requirements
Nice to have
• Would prefer some kind of original pattern/art work/logo rather than an image, not fussed if its very simple/basic
• I am open to any colour but think I would prefer a more earthy sandy clay etc type style than the greens that are commonly associated with naturopathy.
Should not have
• Don't really want to have generic stock images on it

```html
<!DOCTYPE html>
<html lang="en">
<head>
<meta charset="utf-8">
<title>Tom Welby Naturopath – Business Card</title>
<link rel="stylesheet" href="https://fonts.googleapis.com/css2?family=Questrial&display=swap">
<style>
  :root {
    --backdrop: #e9e5dc;
    --card-white: #ffffff;
    --olive-light: #6e6749;
    --olive-dark: #3d3829;
    --sand-gold: #cbbb8c;
    --olive-text: #7a6a36;
    --slate: #6a6a6a;
    --ink: #222222;
  }
  * { box-sizing: border-box; margin: 0; padding: 0; }
  html, body {
    width: 1200px;
    height: 1020px;
    overflow: hidden;
    background: var(--backdrop);
    font-family: "Questrial", "Century Gothic", sans-serif;
  }
  .sheet {
    width: 1200px;
    height: 1020px;
    display: flex;
    flex-direction: column;
    align-items: center;
    justify-content: space-evenly;
  }
  .card {
    width: 840px;
    height: 480px;
    position: relative;
    box-shadow: 0 6px 18px rgba(60, 50, 30, 0.25);
    display: flex;
    flex-direction: column;
    align-items: center;
  }
  /* Back side */
  .card--back {
    background: linear-gradient(160deg, var(--olive-light) 0%, #575036 50%, var(--olive-dark) 100%);
    color: var(--sand-gold);
    padding-top: 110px;
  }
  .brand-mark {
    display: flex;
    align-items: center;
    gap: 12px;
    font-size: 30px;
    letter-spacing: 1px;
  }
  .brand-mark__dot {
    width: 22px;
    height: 22px;
    border-radius: 50%;
    background: currentColor;
  }
  .card--back .brand-mark { color: var(--sand-gold); }
  .back-name {
    margin-top: 46px;
    font-size: 56px;
    letter-spacing: 2px;
    line-height: 1;
  }
  .back-role {
    margin-top: 6px;
    font-size: 20px;
    letter-spacing: 9px;
    padding-left: 70px;
  }
  .back-web {
    position: absolute;
    bottom: 52px;
    right: 56px;
    font-size: 22px;
    letter-spacing: 1px;
  }
  /* Front side */
  .card--front {
    background: linear-gradient(120deg, #ffffff 0%, #ffffff 55%, #ececec 100%);
    padding-top: 78px;
  }
  .card--front .brand-mark { color: var(--olive-text); }
  .front-name {
    margin-top: 64px;
    font-size: 46px;
    color: var(--slate);
    letter-spacing: 1px;
    line-height: 1;
  }
  .front-credentials {
    margin-top: 14px;
    font-size: 21px;
    color: var(--olive-text);
  }
  .contact-row {
    margin-top: 40px;
    display: flex;
    gap: 48px;
    font-size: 24px;
    color: var(--ink);
  }
  .contact-item {
    display: flex;
    align-items: center;
    gap: 12px;
  }
  .contact-item svg { fill: var(--olive-dark); }
</style>
</head>
<body>
<main class="sheet">
  <section class="card card--back" aria-label="Card back">
    <div class="brand-mark"><span class="brand-mark__dot"></span>Tom Welby</div>
    <h1 class="back-name">Tom Welby</h1>
    <p class="back-role">Naturopath</p>
    <p class="back-web">www.tomwelbynaturopathy.com.au</p>
  </section>

  <section class="card card--front" aria-label="Card front">
    <div class="brand-mark"><span class="brand-mark__dot"></span>Tom Welby</div>
    <h2 class="front-name">Tom Welby</h2>
    <p class="front-credentials">NaturopathBHSc (Naturopathy) Member PHRA</p>
    <div class="contact-row">
      <span class="contact-item">
        <svg width="28" height="22" viewBox="0 0 28 22" aria-hidden="true">
          <path d="M2 7 Q14 -1 26 7 L24 10 L19 8 L19 5 Q14 3 9 5 L9 8 L4 10 Z"/>
          <path d="M8 10 L20 10 L25 20 L3 20 Z"/>
        </svg>
        0492 815 306
      </span>
      <span class="contact-item">
        <svg width="30" height="20" viewBox="0 0 30 20" aria-hidden="true">
          <rect x="1" y="1" width="28" height="18" fill="none" stroke="#3d3829" stroke-width="2"/>
          <path d="M1 1 L15 12 L29 1" fill="none" stroke="#3d3829" stroke-width="2"/>
        </svg>
        tom.welby@mailbright.com
      </span>
    </div>
  </section>
</main>
</body>
</html>
```